Beautiful Quotes For Social Media Posts

We are looking for 5 beautifully designed quotes for our social media account.

Inspiration of styles we like in both style and color along with a few of our favorite fonts (you are NOT limited to these fonts this is just to give you an idea):
https://quillmorestudio.example.com/s/k7p2vx9tqa41mzn8wbd3ce6hr5lf0y2j

*These fonts are property of Quillmore Studio. You do not have permission/rights to use them outside of this assignment*

Quotes to use (5):
“Only those who dare to fail greatly can ever achieve greatly.” –Vernon T. Ashgrove
“Don’t go through life, grow through life.” – Milo Pendrake
“Follow your bliss and the universe will open doors where there were only walls.” – Arthur Venholm
“If you don’t like the road you’re walking, start paving another one.” – Greta Mossley
“Life is like riding a bicycle. To keep your balance, you must keep moving.” —Lucian Thornwick

File Specifics:
- JPG
- 10x10 in size (square)
- Please include @QuillmoreStudio in the bottom right left or center of each design

Brand Details:
Soft but rich pastel and bright colors.
Hand Drawn florals, doodles and art
Handwritten looking fonts
Artsy, Creative, Girl and Inspiring

```html
<!DOCTYPE html>
<html lang="en">
<head>
<meta charset="utf-8">
<title>Life Is Like Riding a Bicycle – Quote Post</title>
<link rel="stylesheet" href="https://fonts.googleapis.com/css2?family=Amatic+SC:wght@700&family=Great+Vibes&family=Sacramento&display=swap">
<style>
  :root {
    --paper: #ffffff;
    --teal: #6dd0c8;
    --pink: #fec0c4;
    --teal-wash: rgba(109, 208, 200, 0.16);
    --pink-wash: rgba(254, 192, 196, 0.20);
    --ink: #1d1d1d;
  }
  * { margin: 0; padding: 0; box-sizing: border-box; }
  html, body {
    width: 1200px;
    height: 1200px;
    overflow: hidden;
    background: var(--paper);
  }
  .post {
    position: relative;
    width: 1200px;
    height: 1200px;
    background: var(--paper);
    overflow: hidden;
  }
  .bicycle-pattern {
    position: absolute;
    inset: 0;
    background:
      radial-gradient(circle at 8% 12%, var(--pink-wash) 0, transparent 14%),
      radial-gradient(circle at 24% 5%, var(--teal-wash) 0, transparent 12%),
      radial-gradient(circle at 52% 10%, var(--pink-wash) 0, transparent 13%),
      radial-gradient(circle at 75% 20%, var(--teal-wash) 0, transparent 13%),
      radial-gradient(circle at 30% 24%, var(--pink-wash) 0, transparent 12%),
      radial-gradient(circle at 95% 32%, var(--pink-wash) 0, transparent 12%),
      radial-gradient(circle at 3% 43%, var(--teal-wash) 0, transparent 11%),
      radial-gradient(circle at 87% 50%, var(--teal-wash) 0, transparent 12%),
      radial-gradient(circle at 11% 73%, var(--pink-wash) 0, transparent 12%),
      radial-gradient(circle at 44% 76%, var(--teal-wash) 0, transparent 12%),
      radial-gradient(circle at 83% 80%, var(--pink-wash) 0, transparent 12%),
      radial-gradient(circle at 16% 95%, var(--teal-wash) 0, transparent 11%),
      radial-gradient(circle at 58% 96%, var(--teal-wash) 0, transparent 11%),
      radial-gradient(circle at 98% 92%, var(--pink-wash) 0, transparent 10%);
  }
  .quote {
    position: absolute;
    left: 0;
    width: 1200px;
    text-align: center;
    font-family: "Amatic SC", cursive;
    font-weight: 700;
    font-size: 94px;
    line-height: 1;
    letter-spacing: 2px;
    white-space: nowrap;
  }
  .quote--teal { color: var(--teal); }
  .quote--pink { color: var(--pink); }
  .line-1 { top: 366px; }
  .line-2 { top: 480px; }
  .line-3 { top: 596px; }
  .line-4 { top: 712px; }
  .attribution {
    position: absolute;
    right: 222px;
    top: 818px;
    font-family: "Great Vibes", cursive;
    font-size: 60px;
    color: var(--teal);
    white-space: nowrap;
  }
  .handle {
    position: absolute;
    right: 62px;
    top: 1128px;
    font-family: "Sacramento", cursive;
    font-size: 40px;
    color: var(--ink);
    white-space: nowrap;
  }
</style>
</head>
<body>
  <main class="post">
    <div class="bicycle-pattern" role="img" aria-label="Scattered pattern of pink and teal line-drawn bicycles and small scribbled roses"></div>

    <p class="quote quote--teal line-1">Life is like</p>
    <p class="quote quote--pink line-2">Riding a bicycle.</p>
    <p class="quote quote--teal line-3">To keep your balance,</p>
    <p class="quote quote--pink line-4">You must keep moving</p>

    <p class="attribution">– Lucian Thornwick</p>
    <p class="handle">@QuillmoreStudio</p>
  </main>
</body>
</html>
```